依頼概要
■依頼の目的/概要
大型施設の共有スペースに展示する商品のPOPのデザインをお願いします。
展示の全体イメージがありますのでそれに合わせたイメージで制作して下さい。

■依頼詳細
大型SC内の新店舗の商品展示用のPOPになります。
展示イメージに合うようにPOPの制作をして下さい。
前回の展示のPOPを参考にアップしておきますが、同じような配置にする必要はございません。
前回は背景色などは変えずに、商品名、金額等を、レディース、メンズ、キッズの三種類に色分けして区別しておりました。
今回はキッズはないのですが、レディース、メンズ、雑貨と別れておりますので、うまく区別できるような工夫をお願いします。
サイズは A4縦サイズ。
店舗によって商品、金額、アイテム数は変化するので、変更できるような仕様にして下さい。
フォントはモリサワでしたら入っております。
採用後は使用フォントを納品データと共にお知らせください。

■重視する点
Illustrator・Photoshopの経験必須でお願いします。
新店舗のPOPになりますので、」お客様の目に留まるようなデザインが望ましいです。

■継続依頼について
弊社ではこういった案件が多くあり、次回は母の日、父の日等もありますので、継続的依頼できるありがたいです。

その他何かご不明な点がございましたら、お気軽にご質問下さい。
よろしくお願いいたします。
参考用イメージをアップします。

今回の展示イメージ
前回のPOPイメージ

の2点です。
1店舗の最大アイテム数は6になります。
前回のPOP参考例はあくまで参考です。
同じように作作らなくても良いので参考程度にして頂ければ幸いです。
展示イメージにある通り、POPは各マネキン、雑貨の前に置くものになります。
新店舗のオープンなのでワクワクするようなイメージで制作してもらえればと思います。
集まりが少ないので当選額を上乗せします。
それに伴い期間も延長いたします。
ご応募いただきありがとうございました。

見やすくイメージに沿っていたため。

たくさんのご参加ありがとうございました。
ぜひ次回もご参加下さい。

```html
<!DOCTYPE html>
<html lang="ja">
<head>
<meta charset="UTF-8">
<title>店舗POP レディース</title>
<link href="https://fonts.googleapis.com/css2?family=Noto+Sans+JP:wght@400;500;700&display=swap" rel="stylesheet">
<style>
  :root {
    --pink: #e0559a;
    --pink-deep: #d4418a;
    --pink-light: #f3a6c9;
    --pink-pale: #fbe4ef;
    --pink-frame: #f0b3d0;
    --white: #ffffff;
    --ink: #333333;
    --grey: #9a9a9a;
  }
  * { margin: 0; padding: 0; box-sizing: border-box; }
  html, body { width: 849px; height: 1200px; overflow: hidden; }
  body { font-family: "Noto Sans JP", sans-serif; background: var(--white); }
  .pop {
    position: relative;
    width: 849px; height: 1200px;
    background: var(--pink-pale);
    overflow: hidden;
  }
  .awning { position: absolute; left: 0; top: 0; width: 849px; height: 230px; }
  .title {
    position: absolute; left: 0; top: 22px; width: 100%;
    text-align: center; color: var(--white);
    font-size: 92px; font-weight: 500; letter-spacing: 6px;
  }
  .board {
    position: absolute; left: 51px; top: 238px; width: 747px; height: 770px;
    background: var(--pink-frame);
    border-radius: 6px;
  }
  .board-head {
    position: absolute; left: 0; top: 0; width: 100%; height: 64px;
    background: var(--pink);
    border-radius: 6px 6px 0 0;
  }
  .category { position: absolute; left: 0; top: 0; width: 240px; height: 64px; }
  .category-name {
    position: absolute; left: 22px; top: 6px;
    color: var(--white); font-size: 40px; font-weight: 500;
  }
  .appeal {
    position: absolute; left: 260px; top: 14px;
    color: var(--white); font-size: 27px; font-weight: 400;
  }
  .price-list {
    position: absolute; left: 40px; top: 82px; width: 667px; height: 664px;
    background: var(--white); border-radius: 12px;
    list-style: none;
  }
  .item {
    position: absolute; left: 0; width: 100%; height: 120px;
  }
  .item-name {
    position: absolute; left: 30px; top: 42px;
    font-size: 41px; color: var(--pink-deep); font-weight: 400;
    padding-left: 38px;
  }
  .item-name::before {
    content: ""; position: absolute; left: 0; top: 26px;
    width: 13px; height: 13px; border-radius: 50%;
    background: var(--pink-light);
  }
  .price {
    position: absolute; right: 40px; top: 8px;
    color: var(--pink); font-size: 68px; font-weight: 400; line-height: 1.1;
  }
  .price .yen { font-size: 56px; margin-right: 4px; }
  .tax {
    position: absolute; right: 40px; top: 86px;
    color: var(--ink); font-size: 22px;
  }
  .logo-box {
    position: absolute; left: 23px; top: 1053px; width: 190px; height: 130px;
    background: var(--white); border: 3px solid var(--grey);
  }
  .store-bar {
    position: absolute; left: 249px; top: 1053px; width: 600px; height: 86px;
    background: var(--pink);
    border-radius: 14px 0 0 14px;
    color: var(--white); font-size: 44px; font-weight: 500;
  }
  .store-name { position: absolute; left: 210px; top: 12px; }
  .store-divider { position: absolute; left: 402px; top: 12px; width: 3px; height: 60px; background: var(--white); }
  .store-floor { position: absolute; left: 445px; top: 12px; }
  .corporate-mark {
    position: absolute; right: 22px; top: 1157px;
    font-size: 22px; color: var(--ink);
  }
</style>
</head>
<body>
<main class="pop">
  <svg class="awning" viewBox="0 0 849 230" aria-hidden="true">
    <rect x="0" y="0" width="849" height="230" fill="var(--pink-light)"/>
    <g fill="var(--pink)">
      <rect x="0" y="0" width="60" height="230"/>
      <rect x="120" y="0" width="60" height="230"/>
      <rect x="240" y="0" width="60" height="230"/>
      <rect x="360" y="0" width="60" height="230"/>
      <rect x="480" y="0" width="60" height="230"/>
      <rect x="600" y="0" width="60" height="230"/>
      <rect x="720" y="0" width="60" height="230"/>
      <rect x="840" y="0" width="60" height="230"/>
    </g>
  </svg>
  <h1 class="title">タイトル</h1>

  <section class="board">
    <header class="board-head">
      <svg class="category" viewBox="0 0 240 64" aria-hidden="true">
        <polygon points="0,0 240,0 210,32 240,64 0,64" fill="var(--pink-deep)"/>
      </svg>
      <span class="category-name">Ladies</span>
      <span class="appeal">アピールコメント</span>
    </header>

    <ul class="price-list">
      <li class="item" style="top:30px">
        <span class="item-name">ジャケット</span>
        <span class="price"><span class="yen">¥</span>5,900</span>
        <span class="tax">（税込 ¥6,372）</span>
      </li>
      <li class="item" style="top:190px">
        <span class="item-name">スカート</span>
        <span class="price"><span class="yen">¥</span>4,900</span>
        <span class="tax">（税込 ¥5,292）</span>
      </li>
      <li class="item" style="top:350px">
        <span class="item-name">パンプス</span>
        <span class="price"><span class="yen">¥</span>3,800</span>
        <span class="tax">（税込 ¥4,104）</span>
      </li>
      <li class="item" style="top:510px">
        <span class="item-name">ブラウス</span>
        <span class="price"><span class="yen">¥</span>4,200</span>
        <span class="tax">（税込 ¥4,536）</span>
      </li>
    </ul>
  </section>

  <div class="logo-box" aria-hidden="true"></div>
  <div class="store-bar">
    <span class="store-name">店舗名</span>
    <span class="store-divider"></span>
    <span class="store-floor">階</span>
  </div>
  <p class="corporate-mark">コーポレートロゴ</p>
</main>
</body>
</html>
```